New Car Wrap Design Project

I need to advertise my company using a small car (Brenlo Vix mk2 TQ3) I need to work together with a designer and stylisiing it using multiple logo's and writings. it's no just the logo ! please reach me out
Target Market(s)
Businesses
Requirements
Must have
- Company logo and same font
Nice to have
- details are in the initial message I sent

```html
<!DOCTYPE html>
<html lang="en">
<head>
<meta charset="utf-8">
<title>Lumen Arc – Vehicle Wrap Artwork</title>
<link rel="stylesheet" href="https://fonts.googleapis.com/css2?family=Josefin+Sans:wght@400;700&family=Montserrat:wght@800&display=swap">
<style>
  :root {
    --backdrop: #d8dadb;
    --sage: #a7bbb3;
    --sage-deep: #7f968f;
    --ink: #1c1f1e;
    --white: #ffffff;
    --badge: #7b8c86;
    --violet: #5a3fd0;
    --teal: #3fb9a8;
    --lime: #a9d23c;
    --magenta: #e24a9a;
    --purple: #8b3fd0;
  }
  html, body {
    margin: 0;
    padding: 0;
    overflow: hidden;
  }
  body {
    width: 960px;
    height: 1200px;
    background: var(--backdrop);
    font-family: "Josefin Sans", Arial, sans-serif;
  }
  .wrap-sheet {
    position: relative;
    width: 960px;
    height: 1200px;
  }
  .panel {
    position: absolute;
    left: 40px;
    display: block;
  }
  .panel--side { top: 40px; }
  .panel--rear { top: 610px; }
  .panel-base { fill: var(--sage); }
  .window-zone { fill: var(--sage-deep); }
  .tagline { font-size: 12px; fill: var(--ink); letter-spacing: 0.4px; }
  .tagline-strong { font-weight: 700; }
  .brand-name {
    font-family: "Montserrat", Arial, sans-serif;
    font-weight: 800;
    fill: var(--white);
    font-size: 76px;
    letter-spacing: 1px;
  }
  .brand-name--rear {
    font-family: "Josefin Sans", Arial, sans-serif;
    font-weight: 700;
    font-size: 36px;
    letter-spacing: 2px;
  }
  .brand-dot { fill: var(--white); }
  .phone-pill { fill: var(--white); }
  .phone { font-weight: 700; fill: var(--ink); font-size: 21px; }
  .phone--rear { font-size: 34px; }
  .website { font-weight: 700; fill: var(--ink); font-size: 16px; letter-spacing: 0.5px; }
  .website--rear { font-size: 22px; }
  .service { font-weight: 700; fill: var(--ink); font-size: 12px; letter-spacing: 0.3px; }
  .service--rear { font-size: 16px; }
  .leader { stroke: var(--white); stroke-width: 1.5; stroke-dasharray: 2 4; fill: none; }
  .leader-dot { fill: var(--white); }
  .partner-badge { fill: var(--badge); }
</style>
</head>
<body>
<main class="wrap-sheet">

  <!-- Side panel artwork -->
  <svg class="panel panel--side" width="880" height="500" viewBox="0 0 880 500" aria-label="Side panel artwork">
    <defs>
      <linearGradient id="spectrum-side" x1="0" y1="0.85" x2="1" y2="0.15">
        <stop offset="0" stop-color="var(--violet)"/>
        <stop offset="0.3" stop-color="var(--teal)"/>
        <stop offset="0.6" stop-color="var(--lime)"/>
        <stop offset="0.88" stop-color="var(--magenta)"/>
        <stop offset="1" stop-color="var(--purple)"/>
      </linearGradient>
    </defs>
    <rect class="panel-base" x="0" y="0" width="880" height="500" rx="36"/>
    <path class="spectrum-field" fill="url(#spectrum-side)"
          d="M0,110 Q200,20 440,0 L560,0 L560,200 A170,170 0 0 1 390,370 L0,370 Z"/>

    <text class="tagline" transform="translate(200 150) rotate(-6)">YOUR PARTNER IN IT <tspan class="tagline-strong">INFRASTRUCTURE &amp; AI SOLUTIONS</tspan></text>
    <text class="brand-name" x="36" y="270">LUMEN ARC</text>

    <rect class="phone-pill" x="240" y="392" width="250" height="34" rx="17"/>
    <text class="phone" x="365" y="416" text-anchor="middle">+44 (0) 02079460321</text>

    <g class="partner-row">
      <rect class="partner-badge" x="240" y="446" width="42" height="14" rx="3"/>
      <rect class="partner-badge" x="292" y="446" width="30" height="14" rx="3"/>
      <rect class="partner-badge" x="332" y="446" width="14" height="14" rx="7"/>
      <rect class="partner-badge" x="356" y="446" width="40" height="14" rx="3"/>
      <rect class="partner-badge" x="406" y="446" width="26" height="14" rx="3"/>
      <rect class="partner-badge" x="442" y="446" width="28" height="14" rx="3"/>
    </g>

    <text class="website" transform="translate(630 90) rotate(-6)">WWW.LUMENARC.CO.UK</text>

    <g class="service-list">
      <line class="leader" x1="612" y1="118" x2="612" y2="340"/>
      <circle class="leader-dot" cx="612" cy="118" r="4"/>
      <circle class="leader-dot" cx="612" cy="340" r="4"/>

      <text class="service" x="626" y="158">• AI-DRIVEN IT SOLUTIONS</text>
      <line class="leader" x1="626" y1="172" x2="846" y2="172"/>
      <circle class="leader-dot" cx="848" cy="172" r="4"/>

      <text class="service" x="626" y="200">• DATACENTER INFRASTRUCTURE</text>
      <line class="leader" x1="626" y1="214" x2="836" y2="214"/>
      <circle class="leader-dot" cx="838" cy="214" r="4"/>

      <text class="service" x="626" y="244">• CLOUD, STORAGE, COMPUTE,</text>
      <text class="service" x="637" y="261">NETWORKING AND AI</text>
    </g>
  </svg>

  <!-- Rear panel artwork -->
  <svg class="panel panel--rear" width="880" height="550" viewBox="0 0 880 550" aria-label="Rear panel artwork">
    <defs>
      <linearGradient id="spectrum-rear" x1="0.7" y1="0" x2="0.3" y2="1">
        <stop offset="0" stop-color="var(--violet)"/>
        <stop offset="0.4" stop-color="var(--purple)"/>
        <stop offset="0.55" stop-color="var(--teal)"/>
        <stop offset="1" stop-color="var(--lime)"/>
      </linearGradient>
      <clipPath id="rear-bounds">
        <rect x="0" y="0" width="880" height="550" rx="36"/>
      </clipPath>
    </defs>
    <rect class="panel-base" x="0" y="0" width="880" height="550" rx="36"/>
    <rect class="window-zone" x="130" y="20" width="620" height="210" rx="60"/>

    <g class="rear-logo">
      <circle class="brand-dot" cx="440" cy="82" r="30"/>
      <text class="brand-name brand-name--rear" x="440" y="168" text-anchor="middle">LUMEN ARC</text>
    </g>

    <circle class="spectrum-field" clip-path="url(#rear-bounds)" fill="url(#spectrum-rear)" cx="310" cy="505" r="225"/>

    <text class="website website--rear" x="440" y="262" text-anchor="middle">WWW.LUMENARC.CO.UK</text>
    <text class="phone phone--rear" x="330" y="380" text-anchor="middle">+44 (0) 02079460321</text>

    <g class="service-list">
      <line class="leader" x1="556" y1="350" x2="556" y2="520"/>
      <circle class="leader-dot" cx="556" cy="350" r="5"/>
      <circle class="leader-dot" cx="556" cy="520" r="5"/>

      <text class="service service--rear" x="572" y="400">• AI-DRIVEN IT SOLUTIONS</text>
      <line class="leader" x1="572" y1="416" x2="836" y2="416"/>
      <circle class="leader-dot" cx="840" cy="416" r="5"/>

      <text class="service service--rear" x="572" y="446">• DATACENTER INFRASTRUCTURE</text>
      <line class="leader" x1="572" y1="462" x2="836" y2="462"/>
      <circle class="leader-dot" cx="840" cy="462" r="5"/>

      <text class="service service--rear" x="572" y="494">• CLOUD, STORAGE, COMPUTE,</text>
      <text class="service service--rear" x="585" y="514">NETWORKING AND AI</text>
    </g>
  </svg>

</main>
</body>
</html>
```